COVID-19 Accredited CME Impact Infographic

We want an infographic showing how much COVID-19 Continuing Medical Education we have accredited and its impact. Our website is at https://med.halvering.edu/cme/COVID19/education.html The attached document is intended to simply show the elements. You have complete freedom on design. We will be updating the numbers weekly so it is important that we have the files so that we can update it. This can be done in powerpoint, publisher, word, in-design, illustrator. Don't use crazy fonts that we wont have.

Target Market(s)

Internal to Halvering. We just want to show the impact of our work

Industry/Entity Type

Education

Requirements
Must have
• We must be able to update the numbers ourselves.

See attached document for the pieces that we want.

The sizes of the numbers in the attached are based on importance to us.
Nice to have
• Not mandatory but try to use these colors. https://med.halvering.edu/identity/color-palette.html

I was thinking that perhaps the big number could be done in traditional train. Like this: https://www.pictovane.com/image-illustration/flip-board-under-constuction-page-isolated-8803617452

```html
<!DOCTYPE html>
<html lang="en">
<head>
<meta charset="utf-8">
<title>COVID-19 CME Impact – Halvering Medicine</title>
<link rel="stylesheet" href="https://fonts.googleapis.com/css2?family=Anton&family=Questrial&display=swap">
<style>
  :root {
    --bg: #1b1b1b;
    --label-bg: #070a0c;
    --label-text: #ffffff;
    --title-light: #a8d5d3;
    --title-accent: #1a9aa2;
    --brand: #8c1515;
    --tile-light: #a8d5d3;
    --tile-light-edge: #d9dede;
    --tile-light-digit: #0b2c4d;
    --tile-blue-top: #063566;
    --tile-blue-top-2: #0a5596;
    --tile-blue-bottom: #06305a;
    --tile-blue-edge: #7fd8d8;
    --tile-blue-digit: #ffffff;
  }
  * { box-sizing: border-box; margin: 0; padding: 0; }
  html, body {
    width: 1200px; height: 1100px; overflow: hidden;
    background: var(--bg);
  }
  .infographic {
    position: relative; width: 1200px; height: 1100px;
    font-family: "Questrial", "Century Gothic", sans-serif;
  }
  .title {
    position: absolute; left: 93px; top: 128px;
    font-family: "Anton", "Impact", sans-serif;
    font-size: 102px; line-height: 1; letter-spacing: 1px;
    color: var(--title-light);
  }
  .title__accent { color: var(--title-accent); }
  .brand {
    position: absolute; left: 822px; top: 142px;
    display: flex; align-items: center; gap: 14px;
    color: var(--brand);
    font-family: "Questrial", "Century Gothic", sans-serif;
    font-size: 38px; line-height: 1.05;
  }
  .brand__mark { width: 58px; height: 72px; background: var(--brand); flex: none; }
  .stat { position: absolute; }
  .stat__label {
    display: block; height: 31px; padding: 0 0 0 22px;
    background: var(--label-bg); color: var(--label-text);
    border-radius: 4px; font-size: 19px; line-height: 33px;
    white-space: nowrap; overflow: hidden;
    margin-bottom: 14px;
  }
  .digits { display: flex; gap: 14px; }
  .tile {
    position: relative; width: 97px; height: 162px; flex: none;
    display: flex; flex-direction: column; justify-content: space-between;
    filter: drop-shadow(0 4px 8px rgba(0,0,0,0.55));
  }
  .tile--gap { margin-left: 16px; }
  .tile__half {
    height: 79px; border-radius: 4px;
    background: var(--tile-light);
    border: 2px solid var(--tile-light-edge);
    box-shadow: inset 0 0 0 1px #5f6b6b;
  }
  .tile__half--bottom { border-color: #8a9494; }
  .tile__digit {
    position: absolute; inset: 0;
    display: flex; align-items: center; justify-content: center;
    font-size: 124px; line-height: 1; padding-bottom: 4px;
    color: var(--tile-light-digit);
  }
  .tile--blue .tile__half {
    background: linear-gradient(135deg, var(--tile-blue-top) 0%, var(--tile-blue-top-2) 100%);
    border-color: var(--tile-blue-edge);
    box-shadow: none;
  }
  .tile--blue .tile__half--bottom {
    background: linear-gradient(180deg, var(--tile-blue-bottom) 0%, #05335f 100%);
    border: none; border-top: 2px solid #1e6c98;
  }
  .tile--blue .tile__digit { color: var(--tile-blue-digit); }

  .stat--states { left: 93px; top: 268px; }
  .stat--states .stat__label { width: 173px; }
  .stat--countries { left: 346px; top: 268px; }
  .stat--countries .stat__label { width: 173px; }
  .stat--activities { left: 677px; top: 268px; }
  .stat--activities .stat__label { width: 173px; }
  .stat--cme { left: 93px; top: 535px; }
  .stat--cme .stat__label { width: 204px; }
  .stat--cme .tile--gap { margin-left: 29px; }
  .stat--live { left: 677px; top: 535px; }
  .stat--live .stat__label { width: 204px; }
  .stat--views { left: 93px; top: 793px; }
  .stat--views .stat__label { width: 364px; }
  .stat--views .digits { gap: 17px; }
  .stat--views .tile--gap { margin-left: 26px; }
</style>
</head>
<body>
<main class="infographic">
  <h1 class="title">COVID-19<span class="title__accent">CME</span></h1>
  <div class="brand"><span class="brand__mark"></span><span class="brand__name">Halvering<br>Medicine</span></div>

  <section class="stat stat--states">
    <div class="stat__label">OF STATES</div>
    <div class="digits">
      <div class="tile"><div class="tile__half"></div><div class="tile__half tile__half--bottom"></div><span class="tile__digit">2</span></div>
      <div class="tile"><div class="tile__half"></div><div class="tile__half tile__half--bottom"></div><span class="tile__digit">6</span></div>
    </div>
  </section>

  <section class="stat stat--countries">
    <div class="stat__label">OF COUNTRIES</div>
    <div class="digits">
      <div class="tile"><div class="tile__half"></div><div class="tile__half tile__half--bottom"></div><span class="tile__digit">1</span></div>
      <div class="tile"><div class="tile__half"></div><div class="tile__half tile__half--bottom"></div><span class="tile__digit">2</span></div>
    </div>
  </section>

  <section class="stat stat--activities">
    <div class="stat__label">OF ACTIVITIES</div>
    <div class="digits">
      <div class="tile tile--blue"><div class="tile__half"></div><div class="tile__half tile__half--bottom"></div><span class="tile__digit">2</span></div>
      <div class="tile tile--blue"><div class="tile__half"></div><div class="tile__half tile__half--bottom"></div><span class="tile__digit">3</span></div>
      <div class="tile tile--gap"><div class="tile__half"></div><div class="tile__half tile__half--bottom"></div></div>
      <div class="tile"><div class="tile__half"></div><div class="tile__half tile__half--bottom"></div></div>
    </div>
  </section>

  <section class="stat stat--cme">
    <div class="stat__label">OF CME LEARNERS</div>
    <div class="digits">
      <div class="tile"><div class="tile__half"></div><div class="tile__half tile__half--bottom"></div><span class="tile__digit">5</span></div>
      <div class="tile"><div class="tile__half"></div><div class="tile__half tile__half--bottom"></div><span class="tile__digit">8</span></div>
      <div class="tile tile--gap"><div class="tile__half"></div><div class="tile__half tile__half--bottom"></div><span class="tile__digit">7</span></div>
      <div class="tile"><div class="tile__half"></div><div class="tile__half tile__half--bottom"></div><span class="tile__digit">9</span></div>
    </div>
  </section>

  <section class="stat stat--live">
    <div class="stat__label">OF LIVE LEARNERS</div>
    <div class="digits">
      <div class="tile tile--blue"><div class="tile__half"></div><div class="tile__half tile__half--bottom"></div><span class="tile__digit">2</span></div>
      <div class="tile tile--blue"><div class="tile__half"></div><div class="tile__half tile__half--bottom"></div><span class="tile__digit">3</span></div>
      <div class="tile tile--gap"><div class="tile__half"></div><div class="tile__half tile__half--bottom"></div><span class="tile__digit">1</span></div>
      <div class="tile"><div class="tile__half"></div><div class="tile__half tile__half--bottom"></div><span class="tile__digit">2</span></div>
    </div>
  </section>

  <section class="stat stat--views">
    <div class="stat__label">OF TOTAL ON-DEMAND VIEWS</div>
    <div class="digits">
      <div class="tile tile--blue"><div class="tile__half"></div><div class="tile__half tile__half--bottom"></div><span class="tile__digit">1</span></div>
      <div class="tile tile--blue"><div class="tile__half"></div><div class="tile__half tile__half--bottom"></div><span class="tile__digit">2</span></div>
      <div class="tile tile--blue tile--gap"><div class="tile__half"></div><div class="tile__half tile__half--bottom"></div><span class="tile__digit">0</span></div>
      <div class="tile tile--blue"><div class="tile__half"></div><div class="tile__half tile__half--bottom"></div><span class="tile__digit">9</span></div>
      <div class="tile tile--blue"><div class="tile__half"></div><div class="tile__half tile__half--bottom"></div><span class="tile__digit">9</span></div>
      <div class="tile tile--blue"><div class="tile__half"></div><div class="tile__half tile__half--bottom"></div><span class="tile__digit">8</span></div>
      <div class="tile tile--blue"><div class="tile__half"></div><div class="tile__half tile__half--bottom"></div><span class="tile__digit">7</span></div>
      <div class="tile tile--blue"><div class="tile__half"></div><div class="tile__half tile__half--bottom"></div></div>
      <div class="tile tile--blue"><div class="tile__half"></div><div class="tile__half tile__half--bottom"></div></div>
    </div>
  </section>
</main>
</body>
</html>
```